Business Card - MosswickTreasury.com

I need a business card that has my photo. It should say: My Pemakino store can be found on at the MosswickTreasury.com. Also find my links to Linkhall, Reelcast and Clipbeat. (If this can be done graphically, then that's even better)

```html
<!DOCTYPE html>
<html lang="en">
<head>
<meta charset="utf-8">
<title>Mosswick Treasury – Business Card</title>
<link rel="stylesheet" href="https://fonts.googleapis.com/css2?family=Didact+Gothic&family=Arimo:wght@400;700&display=swap">
<style>
  :root {
    --stage: #c9c9c9;
    --card-front: #ffffff;
    --card-back: #262626;
    --brand-grey: #8a8a88;
    --text-dark: #3a3a3a;
    --rule: #9a9a9a;
    --photo-frame: #b9b9b4;
    --photo-dark: #4a4a4a;
    --photo-warm: #c9a23a;
    --white: #ffffff;
    --social-blue: #2f4f8f;
    --social-red: #d42a2a;
    --social-black: #111111;
  }
  * { box-sizing: border-box; margin: 0; padding: 0; }
  html, body { width: 1200px; height: 800px; overflow: hidden; }
  body {
    background: var(--stage);
    font-family: "Arimo", Arial, sans-serif;
    position: relative;
  }
  .card {
    position: absolute;
    width: 540px;
    height: 310px;
    top: 245px;
    box-shadow: 0 6px 18px rgba(0,0,0,0.18);
    overflow: hidden;
  }
  .card--front { left: 40px; background: var(--card-front); }
  .card--back { left: 620px; background: var(--card-back); }

  /* front */
  .brand {
    position: absolute; left: 34px; top: 52px;
    font-family: "Didact Gothic", sans-serif;
    font-size: 32px; line-height: 1;
    color: var(--brand-grey);
    white-space: nowrap;
  }
  .photo {
    position: absolute; left: 140px; top: 140px;
    width: 210px; height: 150px;
    border: 3px solid var(--photo-frame);
    background: linear-gradient(160deg, var(--photo-dark) 0%, #6a6a6a 55%, var(--photo-warm) 100%);
  }
  .details {
    position: absolute; left: 372px; top: 40px; width: 160px;
    color: var(--text-dark);
  }
  .details__name {
    font-family: "Didact Gothic", sans-serif;
    font-weight: 400;
    font-size: 20px; color: var(--brand-grey); line-height: 1.1;
    white-space: nowrap;
  }
  .details__title { font-size: 12px; margin-top: 3px; }
  .details__rule { height: 1px; background: var(--rule); width: 100px; margin: 10px 0; }
  .contact-list { list-style: none; font-size: 10.5px; line-height: 1.7; }
  .contact-list li { display: flex; align-items: center; gap: 5px; white-space: nowrap; }
  .contact-list svg { width: 10px; height: 10px; flex: none; }
  .social { list-style: none; display: flex; flex-direction: column; gap: 5px; font-size: 10.5px; }
  .social li { display: flex; align-items: center; gap: 6px; }
  .social__dot { width: 12px; height: 12px; border-radius: 50%; }
  .social__dot--blue { background: var(--social-blue); }
  .social__dot--red { background: var(--social-red); }
  .social__dot--black { background: var(--social-black); }

  /* back */
  .back-pattern {
    position: absolute; inset: 0;
    background: linear-gradient(135deg, #2e2e2e 0%, #222 50%, #2b2b2b 100%);
  }
  .back-message {
    position: absolute; left: 0; right: 0; bottom: 70px;
    text-align: center; color: var(--white);
  }
  .back-message__line { font-size: 15px; }
  .back-message__url { font-size: 17px; font-weight: 700; margin-top: 4px; }
</style>
</head>
<body>
  <section class="card card--front">
    <div class="brand">Mosswick Treasury</div>

    <div class="photo" role="img" aria-label="Portrait photo of the store owner"></div>

    <div class="details">
      <h1 class="details__name">Harold Penbury</h1>
      <p class="details__title">Managing Director</p>
      <div class="details__rule"></div>
      <ul class="contact-list">
        <li>
          <svg viewBox="0 0 10 10"><path d="M2 1 L4 1 L4.5 3 L3.3 3.8 Q4.2 5.8 6.2 6.7 L7 5.5 L9 6 L9 8 Q5 9 2 5.5 Q1 3.5 2 1Z" fill="#666"/></svg>
          044-555 018 273
        </li>
        <li>
          <svg viewBox="0 0 10 10"><rect x="0.5" y="2" width="9" height="6" fill="none" stroke="#666"/><path d="M0.5 2 L5 5.5 L9.5 2" fill="none" stroke="#666"/></svg>
          info@mosswickmail.com
        </li>
        <li>
          <svg viewBox="0 0 10 10"><circle cx="5" cy="5" r="4.2" fill="none" stroke="#666"/><path d="M0.8 5 H9.2 M5 0.8 Q2.5 5 5 9.2 M5 0.8 Q7.5 5 5 9.2" fill="none" stroke="#666" stroke-width="0.7"/></svg>
          www.MosswickTreasury.com
        </li>
      </ul>
      <div class="details__rule"></div>
      <ul class="social">
        <li><span class="social__dot social__dot--blue"></span>Linkhall</li>
        <li><span class="social__dot social__dot--red"></span>Reelcast</li>
        <li><span class="social__dot social__dot--black"></span>Clipbeat</li>
      </ul>
    </div>
  </section>

  <section class="card card--back">
    <div class="back-pattern" role="img" aria-label="Tone-on-tone repeating store name pattern on dark background"></div>
    <div class="back-message">
      <p class="back-message__line">My Pemakino store can be found on at the</p>
      <p class="back-message__url">www.MosswickTreasury.com</p>
    </div>
  </section>
</body>
</html>
```